Gently Windswept needs an eye catching marketing flyer

Our new Lumenvale Method(r) business needs an eye catching marketing flyer. We think A5 sizing?
website link (where you can understand more about breathwork is www.gentlywindswept-example.co.uk)
Design whatever you would like to design some things that could be of use to mention are below. Will leave it in your capable hands.
Logo files for Gently Windswept attached, use whichever one is best for your design, should be the main logo and colour scheme for the flyer, the second logo is that of Lumenvale Method(r) the breath school who's body of work we will be delivering. This can be anywhere on the flyer
Flyer is needed to get people interested in breathwork, the potential benefits for breathing better
We offer 1:1 sessions, workshops, corporate training
The flyer will have an offer code 'OpenDoor' which will give 15% off the bookers first 1:1 session
Flyer should include the following contact details: Maybe a "find out how breathwork can help you today. . . "
Carol Pennick (South): 07700 900 318
Rosalind Tarrow (Midlands): 07700 900 742
facebook: we.are.gentlywindswept
instagram: _gentlywindswept_

```html
<!DOCTYPE html>
<html lang="en">
<head>
<meta charset="utf-8">
<title>Gently Windswept – Breathwork Flyer</title>
<link rel="stylesheet" href="https://fonts.googleapis.com/css2?family=Poppins:wght@300;400;500;600;700&family=Oswald:wght@300;400;500&display=swap">
<style>
  :root {
    --ink: #0d1b24;
    --white: #ffffff;
    --sky: #2aa7df;
    --teal: #2ec4d4;
    --indigo: #4b4fc4;
    --violet: #7a4fc0;
    --magenta: #c45aa6;
    --cream: #f6e2c8;
    --brand-gradient: linear-gradient(90deg, #3a55c9 0%, #2ec4d4 30%, #3d56c8 62%, #8a4fbd 85%, #c45aa6 100%);
  }
  * { margin: 0; padding: 0; box-sizing: border-box; }
  html, body { width: 847px; height: 1200px; overflow: hidden; background: var(--ink); }
  .flyer {
    position: relative; width: 847px; height: 1200px; overflow: hidden;
    background: var(--ink); color: var(--white);
    font-family: "Poppins", sans-serif;
  }
  .quote-mark {
    position: absolute; left: 58px; top: 30px;
    font: 700 150px/1 "Poppins", sans-serif;
    background: var(--brand-gradient); -webkit-background-clip: text; background-clip: text; color: transparent;
  }
  .headline { position: absolute; right: 68px; top: 82px; text-align: right; }
  .headline__lead { font: 600 40px/1 "Poppins", sans-serif; letter-spacing: -0.5px; }
  .headline__key {
    font: 700 92px/1 "Poppins", sans-serif; letter-spacing: -3px; margin-top: 8px;
    background: var(--brand-gradient); -webkit-background-clip: text; background-clip: text; color: transparent;
  }
  .headline__tail { font: 600 40px/1 "Poppins", sans-serif; letter-spacing: -0.5px; margin-top: 8px; }

  .brand { position: absolute; left: 208px; top: 400px; width: 350px; height: 350px; }
  .brand__ring { position: absolute; inset: 0; }
  .brand__name {
    position: absolute; left: -20px; right: -80px; top: 60px; text-align: center;
    font: 300 60px/1.15 "Poppins", sans-serif; color: var(--white); letter-spacing: 0.5px;
  }

  .services { position: absolute; left: 40px; right: 40px; top: 778px; height: 132px; display: flex; }
  .service { flex: 1; display: flex; flex-direction: column; align-items: center; }
  .service + .service { border-left: 2px solid var(--white); }
  .service__icon { width: 52px; height: 56px; margin-top: 8px; }
  .service__label {
    margin-top: 22px; text-align: center;
    font: 500 22px/1.2 "Poppins", sans-serif; letter-spacing: 2px; text-transform: uppercase;
  }

  .contacts { position: absolute; left: 58px; top: 968px; display: flex; gap: 30px; }
  .contact__name { font: 400 18px/1 "Poppins", sans-serif; color: var(--sky); text-transform: uppercase; }
  .contact__name strong { font-weight: 600; }
  .contact__area { font-size: 11px; }
  .contact__phone { font: 400 40px/1 "Oswald", sans-serif; margin-top: 10px; letter-spacing: 0.5px; }

  .socials { position: absolute; left: 56px; top: 1066px; display: flex; gap: 14px; align-items: center; font: 400 16px/1 "Poppins", sans-serif; }
  .social { display: flex; align-items: center; gap: 8px; }
  .social__dot { width: 24px; height: 24px; border-radius: 50%; background: var(--sky); }

  .website {
    position: absolute; left: 58px; top: 1104px; width: 540px;
    font: 300 32px/1 "Oswald", sans-serif; color: var(--cream); letter-spacing: 0.5px; white-space: nowrap;
  }

  .offer { position: absolute; left: 619px; top: 965px; width: 172px; }
  .offer__tag {
    height: 26px; border: 2px solid var(--violet); display: flex; align-items: center; justify-content: center; gap: 8px;
    font: 500 14px/1 "Poppins", sans-serif; letter-spacing: 1px;
  }
  .offer__box {
    margin-top: 4px; height: 142px; border: 2px solid var(--indigo); border-bottom: none;
    text-align: center; padding-top: 6px;
  }
  .offer__code { font: 600 23px/1.15 "Poppins", sans-serif; }
  .offer__and { font: 500 12px/1 "Poppins", sans-serif; letter-spacing: 1px; margin-top: 2px; display: flex; align-items: center; justify-content: center; gap: 6px; }
  .rule { display: inline-block; width: 28px; height: 2px; background: var(--white); }
  .offer__amount { font: 600 40px/1.1 "Poppins", sans-serif; }
  .offer__terms { font: 500 13px/1.2 "Poppins", sans-serif; letter-spacing: 0.5px; text-transform: uppercase; margin-top: 2px; }
  .offer__edge { display: block; width: 172px; height: 8px; }
</style>
</head>
<body>
<main class="flyer">
  <div class="quote-mark" aria-hidden="true">&ldquo;</div>

  <header class="headline">
    <p class="headline__lead">Find out how</p>
    <p class="headline__key">breathwork</p>
    <p class="headline__tail">can help you today&hellip;</p>
  </header>

  <section class="brand">
    <svg class="brand__ring" viewBox="0 0 350 350" aria-hidden="true">
      <defs>
        <linearGradient id="ring-grad" x1="0" x2="1" y1="0" y2="1">
          <stop offset="0" stop-color="#2a7fd8"/>
          <stop offset="1" stop-color="#7a4fc0"/>
        </linearGradient>
      </defs>
      <circle cx="175" cy="175" r="172" fill="none" stroke="url(#ring-grad)" stroke-width="2.5"/>
    </svg>
    <h1 class="brand__name">Gently<br>Windswept</h1>
  </section>

  <section class="services">
    <div class="service">
      <svg class="service__icon" viewBox="0 0 52 56" fill="none" stroke="#2aa7df" stroke-width="2.5" aria-hidden="true">
        <rect x="20" y="2" width="12" height="5" rx="1"/>
        <circle cx="26" cy="31" r="20"/>
        <circle cx="26" cy="31" r="14"/>
        <path d="M26 22v9h7"/>
        <path d="M14 52l-3 3M38 52l3 3"/>
      </svg>
      <p class="service__label">1:1 Sessions</p>
    </div>
    <div class="service">
      <svg class="service__icon" viewBox="0 0 52 56" fill="none" stroke="#4b6fd0" stroke-width="2.5" aria-hidden="true">
        <path d="M14 2h24v16l-12 6-12-6z"/>
        <path d="M22 2v18M30 2v18"/>
        <circle cx="26" cy="39" r="14"/>
        <path d="M26 31l2.5 5 5.5.8-4 3.9 1 5.5-5-2.6-5 2.6 1-5.5-4-3.9 5.5-.8z"/>
      </svg>
      <p class="service__label">Corporate<br>Training</p>
    </div>
    <div class="service">
      <svg class="service__icon" viewBox="0 0 52 56" fill="none" stroke="#7a4fc0" stroke-width="2.5" aria-hidden="true">
        <circle cx="26" cy="20" r="17"/>
        <circle cx="26" cy="20" r="12"/>
        <path d="M26 37v12"/>
        <path d="M18 53h16"/>
      </svg>
      <p class="service__label">Workshops</p>
    </div>
  </section>

  <section class="contacts">
    <div class="contact">
      <p class="contact__name">Carol <strong>Pennick</strong> <span class="contact__area">(South)</span></p>
      <p class="contact__phone">07700 900 318</p>
    </div>
    <div class="contact">
      <p class="contact__name">Rosalind <strong>Tarrow</strong> <span class="contact__area">(Midlands)</span></p>
      <p class="contact__phone">07700 900 742</p>
    </div>
  </section>

  <div class="socials">
    <span class="social"><span class="social__dot"></span>we.are.gentlywindswept</span>
    <span class="social"><span class="social__dot"></span>_gentlywindswept_</span>
  </div>

  <p class="website">WWW.GENTLYWINDSWEPT-EXAMPLE.CO.UK</p>

  <aside class="offer">
    <p class="offer__tag"><span class="rule"></span>USE CODE<span class="rule"></span></p>
    <div class="offer__box">
      <p class="offer__code">OpenDoor</p>
      <p class="offer__and"><span class="rule"></span>AND GET<span class="rule"></span></p>
      <p class="offer__amount">15% off</p>
      <p class="offer__terms">The bookers<br>first 1:1 session</p>
    </div>
    <svg class="offer__edge" viewBox="0 0 172 8" aria-hidden="true">
      <polyline fill="none" stroke="#4b4fc4" stroke-width="2" points="1,0 1,4 7,7 13,4 19,7 25,4 31,7 37,4 43,7 49,4 55,7 61,4 67,7 73,4 79,7 85,4 91,7 97,4 103,7 109,4 115,7 121,4 127,7 133,4 139,7 145,4 151,7 157,4 163,7 171,4 171,0"/>
    </svg>
  </aside>
</main>
</body>
</html>
```